Vorna Fleet business card

I am needing a business card that at a glance shows all the services that we provide emphasizing some more than others. We are a Fleet and Compliance management company as well as a software company. We provide outsourced solutions for KPX compliance and HR services via our own software.
In addition, we do
drug testing
GPS
Cameras
Electronic DVIRS
ELD's

Target Market(s)

Transportation company owners

Industry/Entity Type

Transportation supplier

Contact Information for Business Card

the card should inform potential customers what we do

Other font styles liked:
• I have added brand guidelines. See attached

Requirements
Must have
• See description
Should not have
• Colors outside my brand guide. See attached

```html
<!DOCTYPE html>
<html lang="en">
<head>
<meta charset="utf-8">
<title>Vorna Fleet – Business Card</title>
<link href="https://fonts.googleapis.com/css2?family=Montserrat:wght@400;500;600;700;800&display=swap" rel="stylesheet">
<style>
  :root {
    --page-bg: #2a2a2a;
    --card-dark: #1e1e1f;
    --card-light: #ffffff;
    --brand-red: #e8262e;
    --brand-black: #1a1a1a;
    --text-light: #f2f2f2;
    --text-muted: #4a4a4a;
    --rule-light: #d9d9d9;
  }
  html, body {
    margin: 0;
    width: 1200px;
    height: 900px;
    overflow: hidden;
    background: var(--page-bg);
    font-family: "Montserrat", sans-serif;
  }
  .business-card {
    position: absolute;
    left: 110px;
    top: 170px;
    width: 980px;
    height: 560px;
    border-radius: 40px;
    background: var(--card-dark);
    overflow: hidden;
    box-shadow: 0 20px 50px rgba(0,0,0,.45);
  }
  .card-split {
    position: absolute;
    inset: 0;
  }
  .brand-block {
    position: absolute;
    left: 0;
    top: 0;
    width: 540px;
    height: 560px;
    display: flex;
    flex-direction: column;
    align-items: center;
    justify-content: center;
  }
  .brand-lockup {
    display: flex;
    align-items: center;
    gap: 18px;
  }
  .brand-mark {
    width: 34px;
    height: 34px;
    background: var(--brand-red);
  }
  .brand-name {
    font-weight: 800;
    font-size: 58px;
    letter-spacing: 1px;
    color: var(--brand-black);
  }
  .services {
    margin-top: 26px;
    padding-top: 20px;
    width: 420px;
    border-top: 2px solid var(--rule-light);
    text-align: center;
  }
  .services-primary {
    margin: 0 0 10px;
    font-weight: 700;
    font-size: 18px;
    letter-spacing: .5px;
    text-transform: uppercase;
    color: var(--brand-red);
  }
  .services-secondary {
    margin: 0;
    font-weight: 500;
    font-size: 15px;
    line-height: 1.6;
    color: var(--text-muted);
  }
  .contact-block {
    position: absolute;
    left: 612px;
    top: 150px;
    color: var(--text-light);
  }
  .person-name {
    margin: 0;
    font-weight: 700;
    font-size: 30px;
    letter-spacing: .5px;
    text-transform: uppercase;
    color: var(--brand-red);
  }
  .person-title {
    margin: 4px 0 30px;
    font-size: 21px;
    font-weight: 400;
  }
  .address {
    margin: 0 0 30px;
    font-style: normal;
    font-size: 20px;
    line-height: 1.4;
  }
  .contact-list {
    list-style: none;
    margin: 0;
    padding: 0;
    font-size: 20px;
    line-height: 1.55;
  }
  .contact-list li {
    display: flex;
    align-items: center;
    gap: 10px;
  }
  .contact-icon {
    width: 16px;
    height: 16px;
    flex: none;
  }
</style>
</head>
<body>
  <article class="business-card">
    <svg class="card-split" viewBox="0 0 980 560" aria-hidden="true">
      <polygon points="0,0 540,0 540,148 564,168 540,188 540,560 0,560" fill="var(--card-light)"/>
      <polyline points="544,0 544,148 568,168 544,188 544,560" fill="none" stroke="var(--brand-red)" stroke-width="5"/>
    </svg>

    <div class="brand-block">
      <div class="brand-lockup">
        <span class="brand-mark"></span>
        <span class="brand-name">Vorna Fleet</span>
      </div>
      <div class="services">
        <p class="services-primary">KPX Compliance · HR Software</p>
        <p class="services-secondary">Drug Testing · GPS · Cameras<br>Electronic DVIRs · ELDs</p>
      </div>
    </div>

    <div class="contact-block">
      <h1 class="person-name">Daniel Reyes</h1>
      <p class="person-title">Director</p>
      <address class="address">4120 Harbor Loop Rd, Ste B210<br>Portland, OR 97201</address>
      <ul class="contact-list">
        <li>
          <svg class="contact-icon" viewBox="0 0 16 16"><path d="M4 1 L6.5 4.5 L5 6.2 C6 8.2 7.8 10 9.8 11 L11.5 9.5 L15 12 L13 15 C7 14.5 1.5 9 1 3 Z" fill="var(--brand-red)"/></svg>
          555-214-3089
        </li>
        <li>
          <svg class="contact-icon" viewBox="0 0 16 16"><rect x="4" y="1" width="8" height="14" rx="1.5" fill="var(--brand-red)"/><rect x="5.5" y="3" width="5" height="8" fill="var(--card-dark)"/></svg>
          555-214-3090
        </li>
        <li>
          <svg class="contact-icon" viewBox="0 0 16 16"><rect x="1.5" y="3.5" width="13" height="9" fill="none" stroke="var(--brand-red)" stroke-width="1.5"/><polyline points="1.5,3.5 8,9 14.5,3.5" fill="none" stroke="var(--brand-red)" stroke-width="1.5"/></svg>
          info@VornaFleet.com
        </li>
        <li>
          <svg class="contact-icon" viewBox="0 0 16 16"><circle cx="8" cy="8" r="6.5" fill="none" stroke="var(--brand-red)" stroke-width="1.5"/><ellipse cx="8" cy="8" rx="2.8" ry="6.5" fill="none" stroke="var(--brand-red)" stroke-width="1.2"/><line x1="1.5" y1="8" x2="14.5" y2="8" stroke="var(--brand-red)" stroke-width="1.2"/></svg>
          www.VornaFleet.com
        </li>
      </ul>
    </div>
  </article>
</body>
</html>
```